Business Card design

I would like to redo the business cards we have. I want a group card and then individual cards made for each doctor. I like the format of the card attached.

```html
<!DOCTYPE html>
<html lang="en">
<head>
<meta charset="utf-8">
<title>Harbor Ridge Oncology – Business Cards</title>
<link href="https://fonts.googleapis.com/css2?family=Poppins:wght@400;500;600&display=swap" rel="stylesheet">
<style>
  :root {
    --page: #ffffff;
    --panel-grey: #dcdddf;
    --panel-blue: #69abc6;
    --ink-dark: #195a83;
    --ink-light: #3a9fd3;
    --rule: #1d5f88;
  }
  * { box-sizing: border-box; margin: 0; padding: 0; }
  html, body { width: 787px; height: 1200px; overflow: hidden; background: var(--page); }
  body { font-family: "Poppins", sans-serif; color: var(--ink-dark); }
  .sheet { position: relative; width: 787px; height: 1200px; overflow: hidden; }

  .card {
    position: absolute;
    width: 335px; height: 191px;
    display: flex;
    box-shadow: 0 1px 2px rgba(0,0,0,.35);
  }
  .card--left  { left: 25px; }
  .card--right { left: 425px; }

  .brand {
    width: 164px; height: 100%;
    background: var(--panel-grey);
    display: flex; align-items: center;
    padding-left: 12px; gap: 7px;
  }
  .brand__mark { width: 10px; height: 10px; background: var(--ink-dark); flex: none; }
  .brand__name {
    font-weight: 600; font-size: 14.5px; line-height: 1.05;
    color: var(--ink-dark); letter-spacing: .2px;
  }

  .info { position: relative; width: 171px; height: 100%; background: var(--panel-blue); }

  .doctor {
    position: absolute; left: 0; right: 0; top: 21px;
    text-align: center; font-weight: 500; font-size: 11.5px; white-space: nowrap;
  }
  .rule {
    position: absolute; left: 29px; width: 110px; height: 1px;
    background: linear-gradient(90deg, transparent, var(--rule) 30%, var(--rule) 70%, transparent);
  }
  .rule--top { top: 52px; }
  .rule--mid { top: 112px; }
  .cell {
    position: absolute; left: 0; right: 0; top: 72px;
    text-align: center; font-weight: 500; font-size: 14px; white-space: nowrap;
  }

  .roster {
    position: absolute; left: 8px; right: 6px; top: 6px;
    display: grid; grid-template-columns: 1fr 1fr; row-gap: 7.5px;
    font-size: 5.6px; font-weight: 500; white-space: nowrap;
  }
  .roster span:nth-child(even) { text-align: center; }
  .info--group .rule--top { top: 70px; }
  .info--group .cell { top: 82px; }

  .locations {
    position: absolute; left: 14px; right: 4px; top: 127px;
    list-style: none; font-size: 4.1px; line-height: 1.25; font-weight: 500;
  }
  .locations li { position: relative; padding-left: 13px; margin-bottom: 6.5px; }
  .locations li:nth-child(2) { margin-bottom: 8px; }
  .locations li::before {
    content: ""; position: absolute; left: 0; top: 1px;
    width: 4px; height: 4px; border: 0.8px solid var(--ink-dark);
    box-shadow: 0.6px 0.6px 0 var(--ink-dark);
  }
</style>
</head>
<body>
<div class="sheet">

  <!-- Group card -->
  <section class="card card--left" style="top:33px">
    <div class="brand"><span class="brand__mark"></span><p class="brand__name">Harbor Ridge<br>Oncology, PA</p></div>
    <div class="info info--group">
      <div class="roster">
        <span>Daniel R. Whitcomb, M.D.</span><span>Meera Kalvapalli, M.D.</span>
        <span>Peter L. Marsh, M.D.</span><span>Anjali R. Devarakonda, M.D.</span>
        <span>Karim N. Haddad, M.D.</span><span>Daniel Whitcomb, Jr. M.D.</span>
        <span>Leila Rahman, M.D.</span><span>Noor Siddiqui, M.D.</span>
      </div>
      <div class="rule rule--top"></div>
      <p class="cell">Cell (555) 014-2290</p>
      <div class="rule rule--mid"></div>
      <ul class="locations">
        <li>12 Linden Park Drive - Suite 200 - Fairhaven, New Jersey 07100<br>(555) 010-4410 - Fax (555) 010-4450</li>
        <li>Elmwood Outpatient Care Pavilion<br>8 Harbor Avenue - Suite 2 - Westbrook, New Jersey 07040<br>(555) 012-8000 - Fax (555) 012-8340</li>
        <li>450 Mill Road - Ridgefield, New Jersey 07200<br>(555) 019-8817 - Fax (555) 019-8846</li>
      </ul>
    </div>
  </section>

  <section class="card card--right" style="top:33px">
    <div class="brand"><span class="brand__mark"></span><p class="brand__name">Harbor Ridge<br>Oncology, PA</p></div>
    <div class="info">
      <p class="doctor">Noor Siddiqui, M.D.</p>
      <div class="rule rule--top"></div>
      <p class="cell">Cell (555) 014-2290</p>
      <div class="rule rule--mid"></div>
      <ul class="locations">
        <li>12 Linden Park Drive - Suite 200 - Fairhaven, New Jersey 07100<br>(555) 010-4410 - Fax (555) 010-4450</li>
        <li>Elmwood Outpatient Care Pavilion<br>8 Harbor Avenue - Suite 2 - Westbrook, New Jersey 07040<br>(555) 012-8000 - Fax (555) 012-8340</li>
        <li>450 Mill Road - Ridgefield, New Jersey 07200<br>(555) 019-8817 - Fax (555) 019-8846</li>
      </ul>
    </div>
  </section>

  <section class="card card--left" style="top:265px">
    <div class="brand"><span class="brand__mark"></span><p class="brand__name">Harbor Ridge<br>Oncology, PA</p></div>
    <div class="info">
      <p class="doctor">Daniel Whitcomb, Jr. M.D.</p>
      <div class="rule rule--top"></div>
      <p class="cell">Cell (555) 014-2290</p>
      <div class="rule rule--mid"></div>
      <ul class="locations">
        <li>12 Linden Park Drive - Suite 200 - Fairhaven, New Jersey 07100<br>(555) 010-4410 - Fax (555) 010-4450</li>
        <li>Elmwood Outpatient Care Pavilion<br>8 Harbor Avenue - Suite 2 - Westbrook, New Jersey 07040<br>(555) 012-8000 - Fax (555) 012-8340</li>
        <li>450 Mill Road - Ridgefield, New Jersey 07200<br>(555) 019-8817 - Fax (555) 019-8846</li>
      </ul>
    </div>
  </section>

  <section class="card card--right" style="top:264px">
    <div class="brand"><span class="brand__mark"></span><p class="brand__name">Harbor Ridge<br>Oncology, PA</p></div>
    <div class="info">
      <p class="doctor">Anjali R. Devarakonda, M.D.</p>
      <div class="rule rule--top"></div>
      <p class="cell">Cell (555) 014-2290</p>
      <div class="rule rule--mid"></div>
      <ul class="locations">
        <li>12 Linden Park Drive - Suite 200 - Fairhaven, New Jersey 07100<br>(555) 010-4410 - Fax (555) 010-4450</li>
        <li>Elmwood Outpatient Care Pavilion<br>8 Harbor Avenue - Suite 2 - Westbrook, New Jersey 07040<br>(555) 012-8000 - Fax (555) 012-8340</li>
        <li>450 Mill Road - Ridgefield, New Jersey 07200<br>(555) 019-8817 - Fax (555) 019-8846</li>
      </ul>
    </div>
  </section>

  <section class="card card--left" style="top:499px">
    <div class="brand"><span class="brand__mark"></span><p class="brand__name">Harbor Ridge<br>Oncology, PA</p></div>
    <div class="info">
      <p class="doctor">Meera Kalvapalli, M.D.</p>
      <div class="rule rule--top"></div>
      <p class="cell">Cell (555) 014-2290</p>
      <div class="rule rule--mid"></div>
      <ul class="locations">
        <li>12 Linden Park Drive - Suite 200 - Fairhaven, New Jersey 07100<br>(555) 010-4410 - Fax (555) 010-4450</li>
        <li>Elmwood Outpatient Care Pavilion<br>8 Harbor Avenue - Suite 2 - Westbrook, New Jersey 07040<br>(555) 012-8000 - Fax (555) 012-8340</li>
        <li>450 Mill Road - Ridgefield, New Jersey 07200<br>(555) 019-8817 - Fax (555) 019-8846</li>
      </ul>
    </div>
  </section>

  <section class="card card--right" style="top:498px; left:423px">
    <div class="brand"><span class="brand__mark"></span><p class="brand__name">Harbor Ridge<br>Oncology, PA</p></div>
    <div class="info">
      <p class="doctor">Leila Rahman, M.D.</p>
      <div class="rule rule--top"></div>
      <p class="cell">Cell (555) 014-2290</p>
      <div class="rule rule--mid"></div>
      <ul class="locations">
        <li>12 Linden Park Drive - Suite 200 - Fairhaven, New Jersey 07100<br>(555) 010-4410 - Fax (555) 010-4450</li>
        <li>Elmwood Outpatient Care Pavilion<br>8 Harbor Avenue - Suite 2 - Westbrook, New Jersey 07040<br>(555) 012-8000 - Fax (555) 012-8340</li>
        <li>450 Mill Road - Ridgefield, New Jersey 07200<br>(555) 019-8817 - Fax (555) 019-8846</li>
      </ul>
    </div>
  </section>

  <section class="card card--left" style="top:729px">
    <div class="brand"><span class="brand__mark"></span><p class="brand__name">Harbor Ridge<br>Oncology, PA</p></div>
    <div class="info">
      <p class="doctor">Karim N. Haddad, M.D.</p>
      <div class="rule rule--top"></div>
      <p class="cell">Cell (555) 014-2290</p>
      <div class="rule rule--mid"></div>
      <ul class="locations">
        <li>12 Linden Park Drive - Suite 200 - Fairhaven, New Jersey 07100<br>(555) 010-4410 - Fax (555) 010-4450</li>
        <li>Elmwood Outpatient Care Pavilion<br>8 Harbor Avenue - Suite 2 - Westbrook, New Jersey 07040<br>(555) 012-8000 - Fax (555) 012-8340</li>
        <li>450 Mill Road - Ridgefield, New Jersey 07200<br>(555) 019-8817 - Fax (555) 019-8846</li>
      </ul>
    </div>
  </section>

  <section class="card card--right" style="top:729px">
    <div class="brand"><span class="brand__mark"></span><p class="brand__name">Harbor Ridge<br>Oncology, PA</p></div>
    <div class="info">
      <p class="doctor">Peter L. Marsh, M.D.</p>
      <div class="rule rule--top"></div>
      <p class="cell">Cell (555) 014-2290</p>
      <div class="rule rule--mid"></div>
      <ul class="locations">
        <li>12 Linden Park Drive - Suite 200 - Fairhaven, New Jersey 07100<br>(555) 010-4410 - Fax (555) 010-4450</li>
        <li>Elmwood Outpatient Care Pavilion<br>8 Harbor Avenue - Suite 2 - Westbrook, New Jersey 07040<br>(555) 012-8000 - Fax (555) 012-8340</li>
        <li>450 Mill Road - Ridgefield, New Jersey 07200<br>(555) 019-8817 - Fax (555) 019-8846</li>
      </ul>
    </div>
  </section>

  <section class="card card--left" style="top:969px">
    <div class="brand"><span class="brand__mark"></span><p class="brand__name">Harbor Ridge<br>Oncology, PA</p></div>
    <div class="info">
      <p class="doctor">Daniel R. Whitcomb, M.D.</p>
      <div class="rule rule--top"></div>
      <p class="cell">Cell (555) 014-2290</p>
      <div class="rule rule--mid"></div>
      <ul class="locations">
        <li>12 Linden Park Drive - Suite 200 - Fairhaven, New Jersey 07100<br>(555) 010-4410 - Fax (555) 010-4450</li>
        <li>Elmwood Outpatient Care Pavilion<br>8 Harbor Avenue - Suite 2 - Westbrook, New Jersey 07040<br>(555) 012-8000 - Fax (555) 012-8340</li>
        <li>450 Mill Road - Ridgefield, New Jersey 07200<br>(555) 019-8817 - Fax (555) 019-8846</li>
      </ul>
    </div>
  </section>

</div>
</body>
</html>
```